The winning designer MUST include the open diamond between Barlow Tindell to be considered for finalization. We will not consider any designs that do not have the open diamond concept. If you need a link to the image, please email me at mark.barlow@barlowpartnerslaw.example
The front should display the image almost predominantly. Under the main image centered somewhere on the front side should have the website & blog or maybe just the website.
I want the back to have a smaller image of what is on the front, with the exception that the back will have all of the pertinent info such as:
Name -- centered
Office Number - bottom right
Fax - bottom right
email - bottom right
Address - bottom left
email - bottom left
blog - bottom left
https://files.quillmark.example/attachment/u/0/?id=7a3f92c1e4&view=att&ref=58b2c7d0e91f4a63&disp=inline
If this doesn't come out right, let me know and I can email it to you, as it is missing the diamond in the logo I uploaded.
Additionally, I want to see some different color variations in the background, but overall, I want the font and logo design to remain intact.
Marcus T. Barlow
Corwin Tindell
Title should be "Trial Attorney"

```html
<!DOCTYPE html>
<html lang="en">
<head>
<meta charset="utf-8">
<title>Barlow Tindell, PC — Business Cards</title>
<link rel="stylesheet" href="https://fonts.googleapis.com/css2?family=Cinzel:wght@400&family=Open+Sans:wght@300;400&display=swap">
<style>
  :root {
    --backdrop: #e9e7e3;
    --card: #ffffff;
    --ink: #4a4a4a;
    --ink-soft: #8c8c8c;
    --band: #8f8f8f;
    --band-light: #c9c9c9;
    --on-band: #ffffff;
  }
  * { margin: 0; padding: 0; box-sizing: border-box; }
  html, body { width: 1200px; height: 904px; overflow: hidden; }
  body {
    background: var(--backdrop);
    font-family: "Open Sans", Arial, sans-serif;
    color: var(--ink);
    position: relative;
  }
  .card {
    position: absolute;
    width: 680px;
    height: 388px;
    background: var(--card);
    box-shadow: 0 6px 18px rgba(0,0,0,0.18);
    overflow: hidden;
  }
  .card-front { left: 90px; top: 48px; }
  .card-back { left: 430px; top: 468px; }

  .brand {
    position: absolute;
    display: flex;
    align-items: center;
    gap: 12px;
  }
  .brand-mark {
    background: var(--ink);
    flex: none;
  }
  .brand-name {
    font-family: "Cinzel", Georgia, serif;
    font-weight: 400;
    color: var(--ink);
    white-space: nowrap;
  }
  .card-front .brand { left: 150px; top: 146px; }
  .card-front .brand-mark { width: 14px; height: 14px; }
  .card-front .brand-name { font-size: 34px; letter-spacing: 1px; }
  .website {
    position: absolute;
    left: 0; right: 0;
    top: 272px;
    text-align: center;
    font-size: 15px;
    letter-spacing: 1.5px;
    color: var(--ink);
  }

  .card-back .band { position: absolute; inset: 0; }
  .card-back .brand { left: 112px; top: 92px; }
  .card-back .brand-mark { width: 10px; height: 10px; }
  .card-back .brand-name { font-size: 26px; letter-spacing: 1px; }
  .person {
    position: absolute;
    left: 250px; top: 186px;
    text-align: left;
  }
  .person-name { font-size: 19px; font-weight: 400; color: var(--ink); }
  .person-title { font-size: 11px; color: var(--ink-soft); margin-top: 2px; margin-left: 28px; }
  .phones {
    position: absolute;
    right: 26px; top: 214px;
    display: flex; align-items: center; gap: 10px;
    color: var(--on-band);
    font-size: 13px; line-height: 1.35;
  }
  .phones svg { width: 20px; height: 34px; }
  .details {
    position: absolute;
    left: 40px; bottom: 16px;
    color: var(--on-band);
    font-size: 11px; line-height: 1.6;
    list-style: none;
  }
  .details li { display: flex; align-items: center; gap: 6px; }
  .details svg { width: 10px; height: 10px; flex: none; }
</style>
</head>
<body>
  <section class="card card-front" aria-label="Card front">
    <div class="brand">
      <span class="brand-mark"></span>
      <span class="brand-name">Barlow Tindell, PC</span>
    </div>
    <p class="website">barlowtindell.example</p>
  </section>

  <section class="card card-back" aria-label="Card back">
    <svg class="band" viewBox="0 0 680 388" preserveAspectRatio="none" aria-hidden="true">
      <path d="M0 290 C 220 300, 470 250, 680 160 L680 388 L0 388 Z" fill="var(--band-light)"/>
      <path d="M0 302 C 230 312, 480 262, 680 176 L680 388 L0 388 Z" fill="var(--band)"/>
    </svg>
    <div class="brand">
      <span class="brand-mark"></span>
      <span class="brand-name">Barlow Tindell, PC</span>
    </div>
    <div class="person">
      <p class="person-name">Marcus T. Barlow</p>
      <p class="person-title">Trial Attorney</p>
    </div>
    <div class="phones">
      <svg viewBox="0 0 20 34" aria-hidden="true">
        <path d="M3 3 h5 l1 4 -2 2 c1 2 2 3 4 4 l2 -2 4 1 v4 c-8 0-14-6-14-13z" fill="var(--on-band)"/>
        <rect x="3" y="21" width="14" height="11" rx="2" fill="var(--on-band)"/>
      </svg>
      <div>212.555.0174<br>646.555.0121</div>
    </div>
    <ul class="details">
      <li><svg viewBox="0 0 10 10" aria-hidden="true"><circle cx="5" cy="4" r="3" fill="var(--on-band)"/></svg>48 Harbor Row, Suite 615</li>
      <li style="padding-left:16px">Eastport, NY 10090</li>
      <li><svg viewBox="0 0 10 10" aria-hidden="true"><rect x="0.5" y="2" width="9" height="6" fill="none" stroke="var(--on-band)"/></svg>mark@barlowtindell.example</li>
      <li><svg viewBox="0 0 10 10" aria-hidden="true"><rect x="1" y="1" width="8" height="8" fill="var(--on-band)"/></svg>barlowtindellblog.example</li>
    </ul>
  </section>
</body>
</html>
```